A social health network MOBILE APP needs an awesome home page

We need a home page design that is attractive, and simple to navigate for our mobile app. This app helps people maintain their personal health records, find and connect with care providers to ask question, get care online or face to face through appointment. It also has a few other features to encourage engagement such as Forum, Reward, Service Discount Coupon.
We would like to see the design that uses the color green (our company color) as the main color, and includes an area for announcement plus another area for advertising. We include sketches of our need for your review.
The final design should look modern, friendly, and lively.
Updates
If possible, please break away from our attached sketch format and let your creativity leads the way? We would like to see the bottom buttons layout in differently from the sketch.
Industry/Entity Type
Health
Colors
Designer to choose colors to be used in the design.
Requirements
Must have
- A clean and elegant look.

```html
<!DOCTYPE html>
<html lang="vi">
<head>
<meta charset="utf-8">
<title>VitaLink – Home</title>
<link rel="stylesheet" href="https://fonts.googleapis.com/css2?family=Roboto:wght@300;400;500;700;900&family=Oswald:wght@700&display=swap">
<style>
  :root{
    --canvas:#edf1f5;
    --green:#1f9a2e;
    --green-dark:#14801f;
    --green-soft:#eef9ef;
    --green-line:#3aa94a;
    --grid-line:#d6e6d8;
    --ink:#2b2b2b;
    --muted:#8a9a8d;
    --white:#ffffff;
    --navy:#1c2230;
    --orange:#f07a1a;
  }
  *{box-sizing:border-box;margin:0;padding:0}
  html,body{width:1200px;height:1200px;overflow:hidden;background:var(--canvas);font-family:"Roboto",sans-serif;color:var(--ink)}
  .screen{position:absolute;left:350px;top:70px;width:500px;height:1060px;background:var(--white);
    box-shadow:0 20px 50px rgba(40,60,80,.12);overflow:hidden;display:flex;flex-direction:column}

  /* status bar */
  .status-bar{height:28px;background:var(--green);color:var(--white);font-size:12px;display:flex;align-items:center;justify-content:space-between;padding:0 10px}
  .status-bar .left{display:flex;gap:6px;align-items:center}
  .status-bar .right{display:flex;gap:6px;align-items:center}
  .battery{width:24px;height:11px;border:1px solid var(--white);border-radius:2px;padding:1px}
  .battery span{display:block;height:100%;background:var(--white)}

  /* announcement banner */
  .announcement{position:relative;height:240px;background:var(--green);overflow:hidden}
  .announcement .photo{position:absolute;left:0;top:0;width:300px;height:240px;
    background:linear-gradient(135deg,#f1ede6 0%,#e9d7c4 45%,#d9b28e 70%,#f4f1ec 100%)}
  .announcement .wedge{position:absolute;right:0;top:0;width:320px;height:240px;background:var(--green);
    clip-path:polygon(28% 0,100% 0,100% 100%,58% 100%,40% 52%)}
  .announcement .device-photo{position:absolute;right:14px;top:118px;width:150px;height:86px;border-radius:8px;
    background:linear-gradient(120deg,#f7f7f7 0%,#dfe9df 55%,#c99d7a 100%)}
  .announcement .headline{position:absolute;right:18px;top:16px;width:200px;color:var(--white);text-align:left}
  .announcement .brand{font-size:26px;font-weight:700;letter-spacing:.3px}
  .announcement .tagline{font-size:11px;font-weight:500;line-height:1.35;margin-top:4px;text-transform:uppercase}
  .announcement .site-strip{position:absolute;left:0;bottom:0;width:230px;height:30px;background:var(--green-dark);
    display:flex;align-items:center;gap:8px;padding-left:10px;color:var(--white);font-size:11px;font-weight:500}
  .site-strip .dot{width:14px;height:14px;border-radius:50%;background:var(--white)}
  .slider-dots{position:absolute;left:150px;bottom:42px;display:flex;gap:5px}
  .slider-dots i{width:6px;height:6px;border-radius:50%;background:rgba(255,255,255,.6)}
  .slider-dots i.on{background:var(--white)}

  /* primary tiles */
  .primary-actions{display:grid;grid-template-columns:repeat(3,1fr);gap:14px;padding:18px 16px 12px;background:var(--white)}
  .primary-tile{height:132px;border-radius:6px;background:var(--white);box-shadow:0 4px 14px rgba(31,154,46,.14);
    display:flex;flex-direction:column;align-items:center;justify-content:center;gap:12px;position:relative;overflow:hidden}
  .primary-tile::before{content:"";position:absolute;left:-20%;top:-40%;width:140%;height:110%;border-radius:50%;
    background:var(--green-soft);border-bottom:1px dashed #bfe2c3}
  .primary-tile svg{position:relative;width:56px;height:56px}
  .primary-tile .label{position:relative;font-size:15px;font-weight:700;color:var(--green)}

  /* feature grid */
  .feature-grid{display:grid;grid-template-columns:repeat(3,1fr);grid-auto-rows:118px;margin:4px 16px 0;
    border-top:1px dashed var(--grid-line);border-left:1px dashed var(--grid-line)}
  .feature{border-right:1px dashed var(--grid-line);border-bottom:1px dashed var(--grid-line);
    display:flex;flex-direction:column;align-items:center;justify-content:center;gap:10px}
  .feature svg{width:34px;height:34px;fill:none;stroke:var(--green-line);stroke-width:1.4;stroke-linecap:round;stroke-linejoin:round}
  .feature .label{font-size:12px;font-weight:300;color:var(--muted)}

  /* advertising */
  .advert{margin-top:auto;height:186px;display:flex;position:relative;background:var(--navy)}
  .advert .panel-orange{width:110px;background:var(--orange);color:var(--white);padding:12px 10px;font-size:10px;font-weight:700}
  .advert .panel-orange .img{margin-top:10px;height:120px;border-radius:4px;background:linear-gradient(160deg,#f59a4c,#2c3550)}
  .advert .panel-navy{width:100px;background:#252b3a;color:#ffb27a;padding:12px 10px;font-size:18px;font-weight:900}
  .advert .panel-navy .img{margin-top:8px;height:118px;border-radius:4px;background:linear-gradient(160deg,#e9e3da,#b88f6e)}
  .advert .copy{flex:1;padding:22px 20px;color:var(--white)}
  .advert .kicker{font-size:9px;color:#9aa3b5;letter-spacing:.5px}
  .advert .title{font-family:"Oswald",sans-serif;font-size:32px;line-height:1.02;margin-top:8px;text-transform:uppercase}
  .advert .note{font-size:9px;color:#f29a4c;margin-top:8px}
  .advert .sponsor{font-size:11px;color:#c9cfdb;margin-top:10px;display:flex;align-items:center;gap:6px}
  .advert .sponsor i{width:10px;height:10px;border-radius:50%;background:#c9cfdb}
  .advert .pager{position:absolute;left:230px;bottom:12px;display:flex;gap:5px}
  .advert .pager i{width:6px;height:6px;border-radius:50%;background:rgba(255,255,255,.5)}
  .advert .pager i.on{background:var(--green-line)}

  /* tab bar */
  .tab-bar{height:66px;display:flex;border-top:1px solid #e6ece7;background:var(--white)}
  .tab{flex:1;display:flex;flex-direction:column;align-items:center;justify-content:center;gap:4px;font-size:10px;color:var(--muted)}
  .tab svg{width:22px;height:22px;fill:none;stroke:#a7b3aa;stroke-width:1.4;stroke-linejoin:round;stroke-linecap:round}
  .tab.active{color:var(--green)}
  .tab.active svg{fill:var(--green);stroke:var(--green)}
</style>
</head>
<body>
<main class="screen">
  <header class="status-bar">
    <div class="left"><span>●●●●●</span><span>Carrier</span>
      <svg width="14" height="10" viewBox="0 0 14 10" fill="none" stroke="#fff" stroke-width="1.4"><path d="M1 3.5a9 9 0 0 1 12 0M3.5 6a5 5 0 0 1 7 0"/><circle cx="7" cy="8.5" r="1" fill="#fff"/></svg>
    </div>
    <div>9:41 AM</div>
    <div class="right"><span>100%</span><div class="battery"><span></span></div></div>
  </header>

  <section class="announcement">
    <div class="photo" role="img" aria-label="Photo of a smiling family sitting together on a sofa at home"></div>
    <div class="wedge"></div>
    <div class="headline">
      <div class="brand">VitaLink</div>
      <div class="tagline">Sự lựa chọn thông minh<br>bảo vệ sức khỏe cộng đồng</div>
    </div>
    <div class="device-photo" role="img" aria-label="Photo of a hand holding a tablet showing the app"></div>
    <div class="slider-dots"><i class="on"></i><i></i><i></i></div>
    <div class="site-strip"><span class="dot"></span><span>vitalink.vn · Hotline 1900 0000</span></div>
  </section>

  <section class="primary-actions">
    <div class="primary-tile">
      <svg viewBox="0 0 56 56"><path d="M6 16h16l4 5h24v25H6z" fill="#f3c23a"/><path d="M6 24h44l-3 22H9z" fill="#1f9a2e"/><circle cx="28" cy="34" r="5" fill="none" stroke="#fff" stroke-width="2"/></svg>
      <span class="label">Records</span>
    </div>
    <div class="primary-tile">
      <svg viewBox="0 0 56 56"><circle cx="28" cy="26" r="18" fill="#f3c23a"/><circle cx="28" cy="26" r="14" fill="#1f9a2e"/><path d="M22 42l-2 8 9-6z" fill="#f3c23a"/><text x="28" y="32" text-anchor="middle" font-family="Roboto,sans-serif" font-size="16" font-weight="700" fill="#fff">?</text></svg>
      <span class="label">Question</span>
    </div>
    <div class="primary-tile">
      <svg viewBox="0 0 56 56" fill="none" stroke="#1f9a2e" stroke-width="3" stroke-linecap="round"><path d="M10 8v12a10 10 0 0 0 20 0V8"/><path d="M20 30v8a10 10 0 0 0 20 0v-6"/><circle cx="40" cy="26" r="5" fill="#f3c23a" stroke="#1f9a2e"/></svg>
      <span class="label">Find Service</span>
    </div>
  </section>

  <section class="feature-grid">
    <div class="feature">
      <svg viewBox="0 0 34 34"><path d="M5 8h24v15H14l-6 5v-5H5z"/><path d="M10 14h14M10 18h10"/></svg>
      <span class="label">Forum</span>
    </div>
    <div class="feature">
      <svg viewBox="0 0 34 34"><circle cx="9" cy="22" r="3"/><circle cx="25" cy="10" r="3"/><circle cx="25" cy="27" r="3"/><path d="M11.5 20.5l11-8.5M11.5 23.5l11 2.5"/></svg>
      <span class="label">Connections</span>
    </div>
    <div class="feature">
      <svg viewBox="0 0 34 34"><path d="M4 16L30 5l-9 25-5-10z"/><path d="M16 20L30 5"/></svg>
      <span class="label">Invite</span>
    </div>
    <div class="feature">
      <svg viewBox="0 0 34 34"><path d="M4 8h8v6H4zM14 8h8v6h-8zM4 18h8v6H4z"/><circle cx="21" cy="22" r="5"/><path d="M25 26l5 5"/></svg>
      <span class="label">Rewards</span>
    </div>
    <div class="feature">
      <svg viewBox="0 0 34 34"><circle cx="8" cy="24" r="3.5"/><circle cx="8" cy="10" r="3.5"/><path d="M11 12l19 10M11 22l19-10"/><path d="M22 6l-2 3M26 8l-2 3" stroke-dasharray="2 2"/></svg>
      <span class="label">Coupons</span>
    </div>
    <div class="feature">
      <svg viewBox="0 0 34 34"><path d="M5 14h24v5H5zM7 19h20v11H7z"/><path d="M17 14v16"/><path d="M17 14c-3-6-9-5-7-1s7 1 7 1zM17 14c3-6 9-5 7-1s-7 1-7 1z"/></svg>
      <span class="label">Scan Voucher</span>
    </div>
    <div class="feature"></div>
    <div class="feature">
      <svg viewBox="0 0 34 34"><path d="M7 5h20v24H7z"/><path d="M12 5v9l3-2 3 2V5"/></svg>
      <span class="label">Guide</span>
    </div>
    <div class="feature"></div>
  </section>

  <section class="advert" aria-label="Advertising">
    <div class="panel-orange">Casual Shoes
      <div class="img" role="img" aria-label="Product photo of dark sneakers"></div>
    </div>
    <div class="panel-navy">50%
      <div class="img" role="img" aria-label="Product photo of a light leather sneaker"></div>
    </div>
    <div class="copy">
      <div class="kicker">MADE WITH CREATIVE STUDIO</div>
      <div class="title">Shopping<br>HTML 5<br>Banner</div>
      <div class="note">Animated · Responsive</div>
      <div class="sponsor"><i></i>AdSpot</div>
    </div>
    <div class="pager"><i class="on"></i><i></i><i></i><i></i></div>
  </section>

  <nav class="tab-bar">
    <div class="tab active"><svg viewBox="0 0 22 22"><path d="M3 11L11 4l8 7h-3v7H6v-7z"/></svg>Home</div>
    <div class="tab"><svg viewBox="0 0 22 22"><path d="M5 3h12v16H5zM8 8h6M8 12h6M8 15h4"/></svg>Feed</div>
    <div class="tab"><svg viewBox="0 0 22 22"><path d="M6 15V10a5 5 0 0 1 10 0v5l2 2H4zM9 19h4"/></svg>Notification</div>
    <div class="tab"><svg viewBox="0 0 22 22"><path d="M3 5h16v10H9l-4 3v-3H3z"/></svg>Messages</div>
    <div class="tab"><svg viewBox="0 0 22 22"><circle cx="11" cy="11" r="3"/><path d="M11 2v3M11 17v3M2 11h3M17 11h3M4.6 4.6l2.1 2.1M15.3 15.3l2.1 2.1M4.6 17.4l2.1-2.1M15.3 6.7l2.1-2.1"/></svg>Settings</div>
  </nav>
</main>
</body>
</html>
```